Business cards and stationary for mobile catering company
Harvest Kettle
Bright & Fun-filled
Martin Probert
Mobile Catering Proprietor
Fernleigh
Corwen Terrace
Marlowbridge
Kentonshire
KT9 4LP
martin@harvestkettle.co.uk
www.harvestkettle.co.uk
we would like a simple but stylish desing in keeping with our logo
THIS IS OUR LOGO
the . eps file if required

```html
<!DOCTYPE html>
<html lang="en">
<head>
<meta charset="utf-8">
<title>Harvest Kettle – Business Card</title>
<link rel="stylesheet" href="https://fonts.googleapis.com/css2?family=Open+Sans:wght@400;600&display=swap">
<style>
  :root {
    --page-bg: #e9e7e3;
    --card-bg: #ffffff;
    --brand-green: #7cb83a;
    --text-dark: #3a3a3a;
    --text-body: #4a4a4a;
  }
  * { margin: 0; padding: 0; box-sizing: border-box; }
  html, body {
    width: 1200px;
    height: 902px;
    overflow: hidden;
    background: var(--page-bg);
    font-family: "Open Sans", Arial, sans-serif;
  }
  .business-card {
    position: absolute;
    left: 100px;
    top: 165px;
    width: 1000px;
    height: 572px;
    background: var(--card-bg);
    box-shadow: 0 8px 24px rgba(0,0,0,0.18);
  }
  .brand {
    position: absolute;
    left: 70px;
    top: 120px;
    display: flex;
    align-items: center;
    gap: 22px;
  }
  .brand-dot {
    width: 46px;
    height: 46px;
    border-radius: 50%;
    background: var(--brand-green);
  }
  .brand-name {
    font-size: 66px;
    font-weight: 400;
    color: var(--brand-green);
    letter-spacing: -0.5px;
  }
  .person {
    position: absolute;
    right: 70px;
    top: 318px;
    text-align: right;
  }
  .person-name {
    font-size: 27px;
    font-weight: 600;
    color: var(--brand-green);
    line-height: 1.3;
  }
  .person-role {
    font-size: 25px;
    color: var(--text-dark);
    line-height: 1.35;
  }
  .contact-list {
    position: absolute;
    left: 48px;
    top: 362px;
    list-style: none;
    font-size: 18px;
    color: var(--text-body);
    line-height: 28px;
  }
  .contact-item {
    display: flex;
    align-items: flex-start;
    gap: 10px;
  }
  .contact-icon {
    flex: none;
    width: 20px;
    height: 20px;
    margin-top: 4px;
  }
  .contact-icon circle { fill: var(--brand-green); }
  .contact-icon .glyph { fill: #ffffff; }
  .contact-icon .glyph-cut { fill: var(--brand-green); }
  .contact-icon .glyph-line { stroke: #ffffff; fill: none; stroke-width: 1.6; }
  .contact-icon .glyph-fold { stroke: var(--brand-green); fill: none; stroke-width: 1.2; }
</style>
</head>
<body>
  <div class="business-card">
    <div class="brand">
      <span class="brand-dot"></span>
      <span class="brand-name">Harvest Kettle</span>
    </div>

    <div class="person">
      <p class="person-name">Martin Probert</p>
      <p class="person-role">Mobile Catering Proprietor</p>
    </div>

    <ul class="contact-list">
      <li class="contact-item">
        <svg class="contact-icon" viewBox="0 0 20 20" aria-hidden="true">
          <circle cx="10" cy="10" r="10"/>
          <path class="glyph" d="M10 4.5a3.6 3.6 0 0 0-3.6 3.6c0 2.7 3.6 7.1 3.6 7.1s3.6-4.4 3.6-7.1A3.6 3.6 0 0 0 10 4.5zm0 5a1.4 1.4 0 1 1 0-2.8 1.4 1.4 0 0 1 0 2.8z"/>
        </svg>
        <span>Fernleigh Corwen Terrace<br>Marlowbridge Kentonshire<br>KT9 4LP</span>
      </li>
      <li class="contact-item">
        <svg class="contact-icon" viewBox="0 0 20 20" aria-hidden="true">
          <circle cx="10" cy="10" r="10"/>
          <rect class="glyph" x="7" y="4.5" width="6" height="11" rx="1"/>
          <rect class="glyph-cut" x="8" y="6" width="4" height="7"/>
        </svg>
        <span>07700 900412</span>
      </li>
      <li class="contact-item">
        <svg class="contact-icon" viewBox="0 0 20 20" aria-hidden="true">
          <circle cx="10" cy="10" r="10"/>
          <rect class="glyph" x="5" y="6.5" width="10" height="7" rx="0.8"/>
          <path class="glyph-fold" d="M5.3 7l4.7 3.6L14.7 7"/>
        </svg>
        <span>martin@harvestkettle.co.uk</span>
      </li>
      <li class="contact-item">
        <svg class="contact-icon" viewBox="0 0 20 20" aria-hidden="true">
          <circle cx="10" cy="10" r="10"/>
          <circle class="glyph-line" cx="10" cy="10" r="5"/>
          <path class="glyph-line" d="M5 10h10M10 5c-2.2 2.8-2.2 7.2 0 10M10 5c2.2 2.8 2.2 7.2 0 10"/>
        </svg>
        <span>www.harvestkettle.co.uk</span>
      </li>
    </ul>
  </div>
</body>
</html>
```